Job Recruiting Agemcy

almost like my current site www.qulvex.com but with these changes see and what i meant about the across the to the site says home job companies categories pages blog and login sign up that should only be the 4 i said only 1 home 2 industries 3 jobs 4 contact us. and remove latest blog post and our partners because that's not us we have to post acuarte information thanks and the name of the company if your using is is work and premier staffing solutions and want it easy for us to post and remove jobs and where it emails us every resume or person that applies

Requirements
Must have
• must send email to us when an application is submitted and try to incorparate the colors of current site
Nice to have
• i want a pretty basic site for now just like the one i have but with all thats above were its easy for me being the own to be able to post jobs and everything

```html
<!DOCTYPE html>
<html lang="en">
<head>
<meta charset="utf-8">
<title>Qulvex – Work and Premier Staffing Solutions</title>
<link href="https://fonts.googleapis.com/css2?family=Poppins:ital,wght@0,400;0,500;0,600;0,700;1,400&display=swap" rel="stylesheet">
<style>
:root{
  --green:#3d7a59;
  --green-dark:#2f6448;
  --teal:#3397b5;
  --teal-soft:#5cb8d4;
  --navy:#1b2a38;
  --text:#4b5563;
  --muted:#7b8590;
  --hero-bg:#eaf4fb;
  --jobs-bg:#eef7fa;
  --footer-bg:#2b2b2b;
  --white:#ffffff;
  --line:#e6eaee;
}
*{box-sizing:border-box;margin:0;padding:0}
html,body{width:1200px;height:3619px;overflow:hidden}
body{font-family:"Poppins",sans-serif;color:var(--navy);background:var(--white);position:relative}
section,header,footer{position:absolute;left:0;width:1200px}
.abs{position:absolute}

/* hero */
.hero{top:0;height:753px;background:var(--hero-bg);overflow:hidden}
.hero-arc{position:absolute;left:512px;top:-420px;width:1100px;height:1100px;border-radius:50%;background:var(--white)}
.brand{position:absolute;left:88px;top:50px;font-weight:700;font-size:20px;color:var(--green);display:flex;align-items:center;gap:8px}
.brand-dot{width:14px;height:14px;background:var(--teal);border-radius:50%}
.nav{position:absolute;top:34px;left:616px;font-size:14px;font-weight:500}
.nav a{color:var(--navy);text-decoration:none;position:absolute;white-space:nowrap}
.nav a.active{color:var(--teal)}
.login{position:absolute;left:955px;top:34px;font-size:13px;font-weight:500;display:flex;align-items:center;gap:6px}
.signup{position:absolute;left:1034px;top:28px;width:76px;height:31px;background:var(--green);color:#fff;border-radius:3px;font-size:13px;font-weight:600;display:flex;align-items:center;justify-content:center}
.hero-kicker{position:absolute;left:88px;top:304px;color:var(--teal);font-size:22px;font-weight:600}
.hero-title{position:absolute;left:88px;top:332px;font-size:48px;line-height:51px;font-weight:700;color:var(--navy)}
.search{position:absolute;left:88px;top:450px;width:578px;height:59px;background:#fff;border-radius:4px;box-shadow:0 4px 14px rgba(0,0,0,.05)}
.field{position:absolute;top:13px;height:34px;background:#f1f3f5;border-radius:3px;font-size:13px;color:var(--muted);display:flex;align-items:center;gap:8px;padding-left:14px}
.search-btn{position:absolute;left:470px;top:13px;width:98px;height:34px;background:var(--green);color:#fff;border-radius:3px;font-size:13px;font-weight:700;display:flex;align-items:center;justify-content:center}
.hero-visual{position:absolute;left:560px;top:270px;width:650px;height:650px;border-radius:50%;background:radial-gradient(circle at 45% 40%,#4aa8c6,#2e87a6)}
.hero-person{position:absolute;left:640px;top:90px;width:480px;height:663px;border-radius:240px 240px 0 0;background:linear-gradient(180deg,#e9c9a8 0%,#f4f1ee 45%,#d9d3cc 100%);opacity:.9}

/* about */
.about{top:753px;height:560px}
.about-photo{position:absolute;left:88px;top:77px;width:421px;height:371px;background:linear-gradient(135deg,#e3e8ec,#b9c3cb 60%,#8c9aa6)}
.exp-box{position:absolute;left:383px;top:306px;width:149px;height:159px;background:var(--green);color:#fff;padding:24px 0 0 28px}
.exp-box b{display:block;font-size:52px;line-height:56px;font-weight:700}
.exp-box span{display:block;font-size:16px;line-height:20px;font-weight:500}
.about-text{position:absolute;left:634px;top:196px;width:480px}
.about-text h2{font-size:36px;font-weight:700;line-height:44px}
.about-text p{margin-top:16px;font-size:16px;line-height:26px;color:var(--text)}

/* industries */
.industries{top:1290px;height:386px}
.industries h2{position:absolute;left:0;width:1200px;text-align:center;top:20px;font-size:38px;font-weight:600}
.industry{position:absolute;top:110px;width:240px;text-align:center}
.industry-icon{width:106px;height:106px;border-radius:50%;margin:0 auto;position:relative;display:flex;align-items:center;justify-content:center}
.count{position:absolute;right:-4px;top:4px;width:24px;height:24px;border-radius:50%;background:#fff;font-size:11px;color:var(--navy);display:flex;align-items:center;justify-content:center;box-shadow:0 1px 4px rgba(0,0,0,.15)}
.industry h3{margin-top:14px;font-size:16px;font-weight:600}
.industry p{margin-top:2px;font-size:12.5px;line-height:19px;color:var(--text);padding:0 20px}

/* jobs */
.jobs{top:1676px;height:495px;background:var(--jobs-bg)}
.jobs h2{position:absolute;left:0;width:1274px;text-align:center;top:90px;font-size:38px;font-weight:600}
.arrow-btn{position:absolute;top:107px;width:32px;height:26px;border:1px solid #c8d2d9;background:#fff;display:flex;align-items:center;justify-content:center}
.arrow-btn.on{background:var(--teal);border-color:var(--teal)}
.job{position:absolute;top:156px;width:246px;height:245px;background:#fff;padding:28px 24px 0 24px}
.job.featured{border:2px solid var(--teal);padding:26px 22px 0 22px}
.tag{display:inline-block;font-size:11px;font-weight:600;padding:3px 14px;border-radius:3px}
.tag.part{background:#e6f3f8;color:var(--teal)}
.tag.intern{background:#eef0f1;color:var(--navy)}
.tag.full{background:#fdf3df;color:#e5a728}
.job h4{margin-top:10px;font-size:15.5px;line-height:19px;font-weight:600;padding-bottom:12px;border-bottom:1px solid var(--line)}
.meta{margin-top:16px;font-size:12px;line-height:22px;color:var(--text)}
.meta div{display:flex;align-items:center;gap:8px}
.company{position:absolute;left:24px;bottom:30px;right:24px;display:flex;align-items:center;gap:10px;font-size:15px;font-weight:600}
.company .dot{width:32px;height:32px;border-radius:50%;background:var(--teal-soft)}
.company .go{margin-left:auto;width:26px;height:26px;border-radius:50%;background:#f1f3f5;display:flex;align-items:center;justify-content:center}

/* cta */
.cta{top:2171px;height:299px;background:linear-gradient(90deg,#2c6f8f 0%,#2f8fb4 40%,#3aa0c4 100%);overflow:hidden}
.cta-photo{position:absolute;left:0;top:0;width:520px;height:299px;background:linear-gradient(90deg,rgba(20,60,80,.55),rgba(47,143,180,0))}
.cta h2{position:absolute;top:80px;width:1200px;text-align:center;color:#fff;font-size:38px;font-weight:700}
.cta p{position:absolute;top:134px;width:1200px;text-align:center;color:#fff;font-size:17px}
.btn{position:absolute;top:178px;height:40px;display:flex;align-items:center;justify-content:center;font-size:15px;font-weight:700;color:#fff;border-radius:3px}
.btn.solid{left:446px;width:152px;background:var(--green)}
.btn.outline{left:603px;width:152px;border:2px solid #fff}

/* review */
.review{top:2470px;height:738px}
.quote-mark{position:absolute;left:82px;top:90px;font-size:260px;line-height:200px;font-weight:700;color:#e5e7ea;font-style:italic}
.review h2{position:absolute;left:86px;top:305px;font-size:36px;line-height:38px;font-weight:700}
.review blockquote{position:absolute;left:89px;top:390px;width:540px;font-size:16px;line-height:26px;color:var(--text)}
.reviewer{position:absolute;left:89px;top:480px;font-size:15px;font-weight:700;color:var(--green);letter-spacing:.5px}
.role{position:absolute;left:89px;top:502px;font-size:15px;font-style:italic;color:var(--navy)}
.orbits{position:absolute;left:670px;top:95px}
.avatar{position:absolute;border-radius:50%;background:linear-gradient(135deg,#d9c2ad,#8d98a3);border:4px solid #fff;box-shadow:0 6px 16px rgba(0,0,0,.12)}

/* footer */
.footer{top:3208px;height:411px;background:var(--footer-bg);color:#fff}
.footer h2{position:absolute;top:102px;width:1200px;text-align:center;font-size:38px;font-weight:700}
.footer .lead{position:absolute;top:155px;width:1200px;text-align:center;font-size:16px;color:#e4e4e4}
.subscribe{position:absolute;left:308px;top:192px;width:586px;height:43px;background:#fff;border-radius:3px;font-size:14px;color:var(--muted);padding-left:18px;display:flex;align-items:center}
.subscribe-btn{position:absolute;right:0;top:0;width:55px;height:43px;background:var(--green);border-radius:0 3px 3px 0;display:flex;align-items:center;justify-content:center}
.socials{position:absolute;top:254px;left:526px;display:flex;gap:7px}
.socials span{width:32px;height:32px;border-radius:50%;background:#3a3a3a}
.footer-line{position:absolute;left:88px;top:356px;width:1022px;height:1px;background:#444}
.copyright{position:absolute;left:88px;top:377px;font-size:12.5px;font-weight:500}
.links{position:absolute;right:90px;top:377px;display:flex;gap:22px;font-size:12.5px;font-weight:500}
.to-top{position:absolute;left:1145px;top:344px;width:28px;height:28px;border-radius:50%;background:var(--teal);display:flex;align-items:center;justify-content:center}
</style>
</head>
<body>

<header class="hero">
  <div class="hero-arc"></div>
  <svg class="abs" style="left:605px;top:146px" width="200" height="200"><circle cx="98" cy="100" r="84" fill="none" stroke="#3d7a59" stroke-width="26"/></svg>
  <div class="hero-visual" role="img" aria-label="Teal dotted circle backdrop"></div>
  <div class="hero-person" role="img" aria-label="Photo of a smiling young woman holding a laptop"></div>

  <div class="brand"><span class="brand-dot"></span>QULVEX</div>
  <nav class="nav">
    <a class="active" style="left:0">Home</a>
    <a style="left:68px">Industries</a>
    <a style="left:165px">Jobs</a>
    <a style="left:226px">Contact us</a>
  </nav>
  <div class="login">
    <svg width="14" height="14" viewBox="0 0 14 14"><circle cx="7" cy="7" r="7" fill="#1b2a38"/><circle cx="7" cy="5.5" r="2.3" fill="#fff"/><path d="M2.8 11.5c1-2 7.4-2 8.4 0" fill="#fff"/></svg>Login
  </div>
  <div class="signup">Sign Up</div>

  <div class="hero-kicker">Search from 0 job offers</div>
  <h1 class="hero-title">Your career starts<br>here!</h1>
  <div class="search">
    <div class="field" style="left:12px;width:222px">
      <svg width="13" height="13" viewBox="0 0 13 13"><circle cx="5.5" cy="5.5" r="4.3" fill="none" stroke="#7b8590" stroke-width="1.4"/><path d="M8.8 8.8l3 3" stroke="#7b8590" stroke-width="1.4"/></svg>Keyword</div>
    <div class="field" style="left:242px;width:220px">
      <svg width="11" height="14" viewBox="0 0 11 14"><path d="M5.5 13S1 8 1 5.2a4.5 4.5 0 019 0C10 8 5.5 13 5.5 13z" fill="none" stroke="#7b8590" stroke-width="1.3"/><circle cx="5.5" cy="5.2" r="1.6" fill="#7b8590"/></svg>Location</div>
    <div class="search-btn">SEARCH</div>
  </div>
</header>

<section class="about">
  <div class="about-photo" role="img" aria-label="Photo of a recruiter interviewing a candidate at a desk"></div>
  <div class="exp-box"><b>35</b><span>YEARS<br>EXPERIENCE</span></div>
  <div class="about-text">
    <h2>About Us</h2>
    <p>We have over 35 years of Specialized Recruiting and souring experience. We cover a broad spectrum of industries to include some of the top aerospace and pharmaceutical commercial companies of today.</p>
  </div>
</section>

<section class="industries">
  <h2>Industries we support</h2>
  <div class="industry" style="left:96px">
    <div class="industry-icon" style="background:#3397b5">
      <svg width="60" height="40" viewBox="0 0 60 40"><path d="M4 28l52-20-6 10-30 10-8 6-4-2 4-5z" fill="#fff"/><path d="M22 22l8-14h5l-4 11z" fill="#fff"/></svg>
      <span class="count">0</span></div>
    <h3>Aero Space</h3>
    <p>Vantor Aero Controls, Skyforge Corvane Electric</p>
  </div>
  <div class="industry" style="left:352px">
    <div class="industry-icon" style="background:#5cc6e6">
      <svg width="48" height="40" viewBox="0 0 48 40"><rect x="4" y="9" width="40" height="28" rx="4" fill="#fff"/><rect x="17" y="4" width="14" height="7" rx="2" fill="none" stroke="#fff" stroke-width="3"/><circle cx="24" cy="23" r="9" fill="#5cc6e6"/><path d="M22 17h4v4h4v4h-4v4h-4v-4h-4v-4h4z" fill="#fff"/></svg>
      <span class="count">0</span></div>
    <h3>Medical</h3>
    <p>Medora, Vitalon</p>
  </div>
  <div class="industry" style="left:608px">
    <div class="industry-icon" style="background:#6fb3c8">
      <svg width="46" height="50" viewBox="0 0 46 50"><rect x="8" y="4" width="14" height="6" fill="#fff"/><rect x="5" y="12" width="20" height="32" rx="3" fill="#fff"/><rect x="5" y="22" width="20" height="10" fill="#6fb3c8"/><rect x="26" y="34" width="16" height="8" rx="4" transform="rotate(40 34 38)" fill="#fff"/></svg>
      <span class="count">0</span></div>
    <h3>Pharmaceutical</h3>
    <p>Biotechnology Genlume , Corvale cosmetics</p>
  </div>
  <div class="industry" style="left:864px">
    <div class="industry-icon" style="background:#1e7fa3">
      <svg width="52" height="48" viewBox="0 0 52 48"><rect x="4" y="4" width="26" height="32" rx="5" fill="#fff"/><rect x="8" y="10" width="18" height="10" fill="#1e7fa3"/><rect x="22" y="22" width="26" height="18" rx="5" fill="#fff" stroke="#1e7fa3" stroke-width="2"/><rect x="26" y="26" width="18" height="6" fill="#1e7fa3"/></svg>
      <span class="count">0</span></div>
    <h3>Transportation</h3>
    <p>Ridgeway Trucking, Parcelon</p>
  </div>
</section>

<section class="jobs">
  <h2>Recent Jobs</h2>
  <div class="arrow-btn" style="left:1041px"><svg width="8" height="10"><path d="M6 1L2 5l4 4" fill="none" stroke="#1b2a38" stroke-width="1.6"/></svg></div>
  <div class="arrow-btn on" style="left:1079px"><svg width="8" height="10"><path d="M2 1l4 4-4 4" fill="none" stroke="#fff" stroke-width="1.6"/></svg></div>

  <article class="job" style="left:88px">
    <span class="tag part">Part Time</span>
    <h4>Material Production Specialist</h4>
    <div class="meta">
      <div><svg width="9" height="12" viewBox="0 0 11 14"><path d="M5.5 13S1 8 1 5.2a4.5 4.5 0 019 0C10 8 5.5 13 5.5 13z" fill="#9aa3ab"/></svg>San Diego, US</div>
      <div><svg width="10" height="10" viewBox="0 0 10 10"><circle cx="5" cy="5" r="4" fill="none" stroke="#9aa3ab"/><path d="M5 2.5V5h2" fill="none" stroke="#9aa3ab"/></svg>3 Hours ago</div>
    </div>
    <div class="company"><span class="dot"></span>Brightline<span class="go"><svg width="6" height="8"><path d="M1 1l3 3-3 3" fill="none" stroke="#1b2a38" stroke-width="1.3"/></svg></span></div>
  </article>
  <article class="job featured" style="left:347px">
    <span class="tag intern">Internship</span>
    <h4>Site Management Officer</h4>
    <div class="meta">
      <div><svg width="9" height="12" viewBox="0 0 11 14"><path d="M5.5 13S1 8 1 5.2a4.5 4.5 0 019 0C10 8 5.5 13 5.5 13z" fill="#9aa3ab"/></svg>San Diego, US</div>
      <div><svg width="10" height="10" viewBox="0 0 10 10"><circle cx="5" cy="5" r="4" fill="none" stroke="#9aa3ab"/><path d="M5 2.5V5h2" fill="none" stroke="#9aa3ab"/></svg>3 Hours ago</div>
    </div>
    <div class="company"><span class="dot" style="background:#3b5a9a"></span>Northpeak<span class="go"><svg width="6" height="8"><path d="M1 1l3 3-3 3" fill="none" stroke="#1b2a38" stroke-width="1.3"/></svg></span></div>
  </article>
  <article class="job" style="left:606px">
    <span class="tag full">Full Time</span>
    <h4>Business Planner Strategist</h4>
    <div class="meta">
      <div><svg width="9" height="12" viewBox="0 0 11 14"><path d="M5.5 13S1 8 1 5.2a4.5 4.5 0 019 0C10 8 5.5 13 5.5 13z" fill="#9aa3ab"/></svg>San Diego, US</div>
      <div><svg width="10" height="10" viewBox="0 0 10 10"><circle cx="5" cy="5" r="4" fill="none" stroke="#9aa3ab"/><path d="M5 2.5V5h2" fill="none" stroke="#9aa3ab"/></svg>3 Hours ago</div>
    </div>
    <div class="company"><span class="dot"></span>Brightline<span class="go"><svg width="6" height="8"><path d="M1 1l3 3-3 3" fill="none" stroke="#1b2a38" stroke-width="1.3"/></svg></span></div>
  </article>
  <article class="job" style="left:864px">
    <span class="tag part">Part Time</span>
    <h4>Material Production Specialist</h4>
    <div class="meta">
      <div><svg width="9" height="12" viewBox="0 0 11 14"><path d="M5.5 13S1 8 1 5.2a4.5 4.5 0 019 0C10 8 5.5 13 5.5 13z" fill="#9aa3ab"/></svg>San Diego, US</div>
      <div><svg width="10" height="10" viewBox="0 0 10 10"><circle cx="5" cy="5" r="4" fill="none" stroke="#9aa3ab"/><path d="M5 2.5V5h2" fill="none" stroke="#9aa3ab"/></svg>3 Hours ago</div>
    </div>
    <div class="company"><span class="dot"></span>Brightline<span class="go"><svg width="6" height="8"><path d="M1 1l3 3-3 3" fill="none" stroke="#1b2a38" stroke-width="1.3"/></svg></span></div>
  </article>
</section>

<section class="cta">
  <div class="cta-photo" role="img" aria-label="Photo of a smiling woman on a phone call in an office"></div>
  <h2>Seeking For a Job?</h2>
  <p>Browse hundreds of job offers and find the best suitable position.</p>
  <div class="btn solid">SEARCH JOBS</div>
  <div class="btn outline">ADD A RESUME</div>
</section>

<section class="review">
  <div class="quote-mark">“</div>
  <h2>Customer<br>Review</h2>
  <blockquote>I didn't even need training. I couldn't have asked for more than this. It really saves me time and effort. Hireway is exactly what our business has been lacking. I would be lost without Hireway.</blockquote>
  <div class="reviewer">MARA ELLISON</div>
  <div class="role">HR Manager in Orchard Labs</div>
  <svg class="abs" style="left:88px;top:542px" width="84" height="20"><path d="M22 10H2m7-7L2 10l7 7" fill="none" stroke="#b5bcc3" stroke-width="1.6"/><path d="M36 10h44m-7-7l7 7-7 7" fill="none" stroke="#1b2a38" stroke-width="1.6"/></svg>

  <div class="orbits">
    <svg width="570" height="570" style="position:absolute;left:0;top:0"><circle cx="285" cy="287" r="281" fill="none" stroke="#e4e8eb" stroke-width="1.5"/><circle cx="285" cy="287" r="196" fill="none" stroke="#e4e8eb" stroke-width="1.5"/><circle cx="285" cy="287" r="73" fill="none" stroke="#e4e8eb" stroke-width="1.5"/></svg>
    <div class="avatar" role="img" aria-label="Customer portrait" style="left:90px;top:10px;width:42px;height:42px"></div>
    <div class="avatar" role="img" aria-label="Customer portrait" style="left:335px;top:50px;width:40px;height:40px"></div>
    <div class="avatar" role="img" aria-label="Featured customer portrait" style="left:27px;top:130px;width:170px;height:170px"></div>
    <div class="avatar" role="img" aria-label="Customer portrait" style="left:253px;top:170px;width:54px;height:54px"></div>
    <div class="avatar" role="img" aria-label="Customer portrait" style="left:385px;top:225px;width:104px;height:104px"></div>
    <div class="avatar" role="img" aria-label="Customer portrait" style="left:100px;top:320px;width:72px;height:72px"></div>
    <div class="avatar" role="img" aria-label="Customer portrait" style="left:218px;top:330px;width:120px;height:120px"></div>
    <div class="avatar" role="img" aria-label="Customer portrait" style="left:72px;top:420px;width:44px;height:44px"></div>
    <div class="avatar" role="img" aria-label="Customer portrait" style="left:340px;top:465px;width:68px;height:68px"></div>
  </div>
</section>

<footer class="footer">
  <h2>Subscribe Newsletter</h2>
  <div class="lead">Subscribe to Qulvex Pacific newsletter to get the latest jobs posted.</div>
  <div class="subscribe">Enter your email address
    <div class="subscribe-btn"><svg width="18" height="18" viewBox="0 0 18 18"><path d="M1 8l16-7-5 16-3-6z" fill="#fff"/><path d="M9 11l8-10" stroke="#3d7a59" stroke-width="1.2"/></svg></div>
  </div>
  <div class="socials"><span></span><span></span><span></span><span></span></div>
  <div class="footer-line"></div>
  <div class="to-top"><svg width="10" height="8"><path d="M1 6l4-4 4 4" fill="none" stroke="#fff" stroke-width="1.6"/></svg></div>
  <div class="copyright">© 2019 Qulvex. All Rights Reserved.</div>
  <div class="links"><span>Site Map</span><span>Privacy Policy</span><span>Terms of Service</span><span>Security &amp; Privacy</span></div>
</footer>

</body>
</html>
```